Zielgruppe
Ich erstelle und vermarkte hochwertige Ebooks/Taschenbücher über Veltrano. Zielgruppe sind Veltrano Lumio Kunden.
Translate to english with google translater:
I create and market high-quality ebooks/paperbacks via Veltrano. The target group are Veltrano Lumio customers.
Aufgabenstellung
Es geht sowohl um die Gestaltung eines Taschenbuch-Covers als auch um die Gestaltung eines Ebook-Covers.
Die Gesamtaufmachung soll schlicht und in sich stimmig sein, ohne viel Schnörkel.
Der Buchtitel lautet wie folgt: Kochbuch für Hobbyköche, Anfänger, Berufstätige und Studenten
Der Untertitel in etwa halber Schriftgröße lautet wie folgt: Mit den 150 besten und originellsten Rezepten für einen perfekten Einstieg
Pseudonym des Autors am unteren Ende: Matthias Wendrauer
Farbliche Aufmachung: Der Hintergrund ein sehr dunkles Rot, Außen ganz dunkel, nach Innen hin zur Mitte etwas heller in fließendem Übergang. Die Schrift in schlichtem Weiß.
Gestalterische Aufmachung: Normale Schriftart. Ausgenommen 'Kochbuch', 'Kochbuch' in Schriftart ähnlich wie Schriftart Monotype Corsiva. Im unterem Bereich Rechts ein Bild eines bunten originellen Gerichts - Nudelgericht - aus der Vogelperspektive, Links einige Gewürze verstreut und einen echten Kochlöffel in dunklem Braun. Genaue Anordnung überlasse ich dem Designer.
It's about designing a paperback cover as well as designing an ebook cover.
The overall presentation should be simple and coherent, without a lot of frills.
The book title is as follows: Kochbuch für Hobbyköche, Anfänger, Berufstätige und Studenten
The subtitle in about half font size is as follows: Mit den 150 besten und originellsten Rezepten für einen perfekten Einstieg
Author's pseudonym at the bottom: Matthias Wendrauer
Color presentation: The background is a very dark red, very dark on the outside, slightly lighter towards the middle in a flowing transition. The font is plain white.
Design: Normal font. Except 'Kochbuch', 'Kochbuch' in font similar to Monotype Corsiva font. In the lower area on the right a picture of a colorful original dish - pasta dish - from a bird's eye view, on the left some spices scattered around and a real wooden spoon in dar..

```html
<!DOCTYPE html>
<html lang="de">
<head>
<meta charset="utf-8">
<title>Kochbuch – Taschenbuch-Umschlag</title>
<link rel="stylesheet" href="https://fonts.googleapis.com/css2?family=Cormorant+Garamond:ital,wght@0,400;0,500;1,400;1,500&family=Poppins:wght@300;400&display=swap">
<style>
  :root {
    --bg-black: #0a0505;
    --bg-deep: #1c0706;
    --bg-red: #4a120c;
    --bg-glow: #5e1a10;
    --text-white: #f4f1ee;
    --text-gold: #cdb68c;
    --barcode-box: #625c64;
    --photo-warm: #6b3a1c;
    --photo-plate: #d9cdb3;
  }
  * { margin: 0; padding: 0; box-sizing: border-box; }
  html, body { width: 1200px; height: 933px; overflow: hidden; background: var(--bg-black); }
  .cover {
    position: relative;
    width: 1200px; height: 933px;
    overflow: hidden;
    background:
      radial-gradient(ellipse 300px 360px at 300px 330px, rgba(94,26,16,0.85), rgba(74,18,12,0) 100%),
      radial-gradient(ellipse 320px 420px at 880px 330px, rgba(94,26,16,0.8), rgba(74,18,12,0) 100%),
      linear-gradient(90deg, var(--bg-deep) 0%, var(--bg-red) 25%, var(--bg-deep) 50%, var(--bg-red) 75%, var(--bg-deep) 100%);
    color: var(--text-white);
    font-family: "Poppins", sans-serif;
  }
  .cover::after {
    content: "";
    position: absolute; inset: 0;
    background: linear-gradient(180deg, rgba(10,5,5,0.55) 0%, rgba(10,5,5,0) 25%, rgba(10,5,5,0) 55%, rgba(10,5,5,0.85) 100%);
    pointer-events: none;
  }
  .cover > * { position: absolute; z-index: 1; }

  .script-title {
    font-family: "Cormorant Garamond", serif;
    font-style: italic;
    font-weight: 400;
    line-height: 1;
    color: var(--text-white);
  }
  .caps-subtitle {
    font-weight: 400;
    text-transform: uppercase;
    color: var(--text-white);
    line-height: 1.35;
  }

  /* Back cover */
  .back-title { left: 0; width: 594px; top: 58px; text-align: center; font-size: 84px; }
  .back-subtitle { left: 0; width: 594px; top: 136px; text-align: center; font-size: 15.5px; letter-spacing: 1.2px; line-height: 22px; }
  .back-blurb {
    left: 49px; top: 202px; width: 497px;
    font-size: 12.3px; font-weight: 300; letter-spacing: 0.9px;
    line-height: 15.7px; text-align: justify;
  }
  .back-blurb p + p { margin-top: 15.7px; }
  .dish-circle { width: 226px; height: 226px; border-radius: 50%; top: 495px; }
  .dish-circle.cream { left: 61px; background: radial-gradient(circle at 55% 60%, #e9dcb8 0%, #d8d4cf 40%, #bdb9b5 100%); }
  .dish-circle.fusilli { left: 313px; background: radial-gradient(circle at 50% 50%, #b77a3c 0%, #a9683a 30%, #f2efec 58%, #e8e5e2 100%); }
  .barcode-area { left: 325px; top: 754px; width: 229px; height: 138px; background: var(--barcode-box); }

  /* Spine */
  .spine-text {
    left: 602px; top: 466px;
    transform: translate(-50%, -50%) rotate(-90deg);
    white-space: nowrap;
    font-size: 15px; letter-spacing: 1.9px;
  }

  /* Front cover */
  .front-title { left: 700px; width: 410px; top: 72px; text-align: center; font-size: 112px; }
  .front-subtitle { left: 696px; width: 412px; top: 196px; text-align: center; font-size: 23.5px; letter-spacing: 2.3px; line-height: 35px; font-weight: 300; }
  .tagline {
    right: 85px; top: 340px; text-align: right;
    font-family: "Cormorant Garamond", serif; font-style: italic;
    font-size: 25px; line-height: 32px; color: var(--text-gold);
  }
  .tagline .accent { color: var(--text-white); font-weight: 500; }
  .tagline .number { font-size: 38px; font-style: normal; font-weight: 400; }
  .food-photo { left: 560px; top: 470px; width: 640px; height: 463px; }
  .author { left: 700px; width: 402px; top: 882px; text-align: center; font-size: 16px; letter-spacing: 4.2px; text-transform: uppercase; font-weight: 400; }
</style>
</head>
<body>
<main class="cover">
  <!-- Back cover -->
  <h2 class="script-title back-title">Kochbuch</h2>
  <p class="caps-subtitle back-subtitle">Für Hobbyköche, Anfänger,<br>Berufstätige und Studenten</p>
  <div class="back-blurb">
    <p>Die Ernährung hat einen großen Einfluss auf unsere Gesundheit und unser Wohlbefinden. Selbst zu kochen bringt dabei viele Vorteile mit sich und kann zu einem wunderbaren Hobby werden. Im Gegensatz zu Fertigprodukten und Restaurantbesuchen können Sie zudem viel Geld sparen. Im Supermarkt finden Sie von frischem Obst und Gemüse bis hin zu verschiedensten Gewürzen alle Zutaten für die leckeren Gerichte aus unserem Kochbuch.</p>
    <p>Dank der unkomplizierten Rezepte können Sie auch ohne Vorkenntnisse sofort beginnen. Die Zubereitung der Speisen nimmt nur wenig Zeit in Anspruch, wodurch Sie das Kochen problemlos in Ihre Tagesplanung integrieren können. Des Weiteren finden Sie in unserem Kochbuch für Anfänger sowohl Vorspeisen und Hauptgerichte als auch zahlreiche Nachspeisen. So haben Sie für jede Gelegenheit immer ein passendes Rezept parat und können Ihre Fertigkeiten in der Küche Schritt für Schritt entwickeln. Durchstöbern Sie jetzt unser Kochbuch für Anfänger und entdecken Sie Ihre Leidenschaft fürs Kochen.</p>
  </div>
  <div class="dish-circle cream" role="img" aria-label="Foto: Bandnudeln mit heller Rahmsoße auf weißem Teller"></div>
  <div class="dish-circle fusilli" role="img" aria-label="Foto: Fusilli mit Tomaten, Gemüse und Basilikum in weißer Schale, von oben"></div>
  <div class="barcode-area"></div>

  <!-- Spine -->
  <p class="caps-subtitle spine-text">Kochbuch für Hobbyköche, Anfänger, Berufstätige und Studenten</p>

  <!-- Front cover -->
  <h1 class="script-title front-title">Kochbuch</h1>
  <p class="caps-subtitle front-subtitle">Für Hobbyköche, Anfänger,<br>Berufstätige und Studenten</p>
  <p class="tagline">
    Mit den <span class="accent number">150</span><br>
    besten und originellsten <span class="accent">Rezepten</span><br>
    für einen perfekten <span class="accent">Einstieg</span>
  </p>
  <svg class="food-photo" viewBox="0 0 640 463" role="img" aria-label="Foto von oben: Spaghetti mit Tomaten auf einem Teller, Mörser mit Muskatnüssen, verstreute Gewürze und Mehl sowie ein hölzerner Kochlöffel">
    <defs>
      <radialGradient id="spice-haze" cx="0.6" cy="0.45" r="0.55">
        <stop offset="0" stop-color="#8a5a2a" stop-opacity="0.55"/>
        <stop offset="1" stop-color="#3a1208" stop-opacity="0"/>
      </radialGradient>
      <radialGradient id="plate-tone" cx="0.5" cy="0.5" r="0.5">
        <stop offset="0" stop-color="#e0b860"/>
        <stop offset="0.7" stop-color="#c9a25a"/>
        <stop offset="1" stop-color="var(--photo-plate)"/>
      </radialGradient>
    </defs>
    <rect width="640" height="463" fill="url(#spice-haze)"/>
    <circle cx="440" cy="217" r="137" fill="url(#plate-tone)"/>
    <ellipse cx="165" cy="90" rx="58" ry="75" fill="#c8bba6" opacity="0.85"/>
  </svg>
  <p class="author">Matthias Wendrauer</p>
</main>
</body>
</html>
```